Body therapist needs a business card

I need a card for my business which is teaching trainings in body therapy, the company is called Wexcombe Educational Group. I teach to massage therapists around Australia, South East Asia and the USA. I am attaching my logo which will guide you as to what colours I would like to have you consider. Please consult my website to find out more about what I do. www.corvantela.com.au

My name is Daniel Wexcombe. My phone number is (03) 9417 2608 or 0461753208. email is info@corvantela.com.au

```html
<!DOCTYPE html>
<html lang="en">
<head>
<meta charset="utf-8">
<title>Wexcombe Educational Group – Business Card</title>
<link href="https://fonts.googleapis.com/css2?family=Oswald:wght@600&family=Poppins:wght@400;500&display=swap" rel="stylesheet">
<style>
  :root {
    --backdrop: #d9d9d9;
    --card-black: #0b0b0c;
    --card-sheen: #1c1c1e;
    --accent-red: #c8200f;
    --accent-orange: #d2661a;
    --accent-lime: #c9d400;
    --brand-brown: #b4621c;
    --text-light: #d8d8d8;
    --divider: #5a5a5a;
  }
  * { margin: 0; padding: 0; box-sizing: border-box; }
  html, body { width: 1200px; height: 800px; overflow: hidden; }
  body {
    background: var(--backdrop);
    position: relative;
    font-family: "Poppins", sans-serif;
  }
  .card {
    position: absolute;
    width: 540px;
    height: 309px;
    background: linear-gradient(135deg, var(--card-sheen) 0%, var(--card-black) 45%, var(--card-black) 100%);
    box-shadow: 0 14px 30px rgba(0,0,0,0.25);
    overflow: hidden;
  }
  .card--contact { left: 60px; top: 70px; }
  .card--brand { left: 600px; top: 420px; }

  /* contact side */
  .edge-band {
    position: absolute;
    left: 0; right: 0; bottom: 0;
    height: 12px;
    background: linear-gradient(90deg, var(--accent-red) 0%, var(--accent-orange) 22%, var(--accent-lime) 50%, var(--accent-orange) 80%, var(--accent-red) 100%);
  }
  .contact-block {
    position: absolute;
    left: 0; right: 0; top: 0; bottom: 12px;
    display: flex;
    align-items: center;
    justify-content: center;
    gap: 26px;
  }
  .holder-name {
    font-family: "Oswald", sans-serif;
    font-weight: 600;
    font-size: 25px;
    letter-spacing: 0.5px;
    text-transform: uppercase;
    color: var(--accent-red);
  }
  .divider {
    width: 1px;
    height: 64px;
    background: var(--divider);
  }
  .contact-list { list-style: none; }
  .contact-list li {
    display: flex;
    align-items: center;
    gap: 9px;
    font-size: 13px;
    line-height: 19px;
    color: var(--text-light);
  }
  .contact-list svg { width: 11px; height: 11px; fill: var(--accent-red); flex: none; }

  /* brand side */
  .brand-lockup {
    position: absolute;
    left: 0; right: 0; top: 0; bottom: 4px;
    display: flex;
    align-items: center;
    justify-content: center;
    gap: 18px;
  }
  .brand-dot {
    width: 64px; height: 64px;
    border-radius: 50%;
    background: var(--accent-lime);
    flex: none;
  }
  .brand-name {
    font-weight: 500;
    font-size: 27px;
    line-height: 1.2;
    color: var(--brand-brown);
  }
  .base-line {
    position: absolute;
    left: 0; right: 0; bottom: 0;
    height: 4px;
    background: var(--accent-lime);
  }
</style>
</head>
<body>

  <section class="card card--contact" aria-label="Business card, contact side">
    <div class="contact-block">
      <h1 class="holder-name">Daniel Wexcombe</h1>
      <span class="divider"></span>
      <ul class="contact-list">
        <li>
          <svg viewBox="0 0 24 24" aria-hidden="true"><path d="M6.6 10.8a15 15 0 0 0 6.6 6.6l2.2-2.2c.3-.3.7-.4 1-.2 1.1.4 2.3.6 3.6.6.6 0 1 .4 1 1V20c0 .6-.4 1-1 1A17 17 0 0 1 3 4c0-.6.4-1 1-1h3.5c.6 0 1 .4 1 1 0 1.3.2 2.5.6 3.6.1.3 0 .7-.2 1z"/></svg>
          (03) 9417 2608
        </li>
        <li>
          <svg viewBox="0 0 24 24" aria-hidden="true"><path d="M7 1h10c1.1 0 2 .9 2 2v18c0 1.1-.9 2-2 2H7c-1.1 0-2-.9-2-2V3c0-1.1.9-2 2-2zm0 3v14h10V4zm5 15.5a1.2 1.2 0 1 0 0 2.4 1.2 1.2 0 0 0 0-2.4z"/></svg>
          0461753208
        </li>
        <li>
          <svg viewBox="0 0 24 24" aria-hidden="true"><path d="M2 5h20v14H2zm2 2v.5l8 5 8-5V7zm0 2.8V17h16V9.8l-8 5z"/></svg>
          info@corvantela.com.au
        </li>
        <li>
          <svg viewBox="0 0 24 24" aria-hidden="true"><path d="M12 2a10 10 0 1 0 0 20 10 10 0 0 0 0-20zm7.9 9h-3.4a15 15 0 0 0-1.6-6.4A8 8 0 0 1 19.9 11zM12 4c1 1.3 2.3 3.8 2.5 7h-5C9.7 7.8 11 5.3 12 4zM4.1 13h3.4a15 15 0 0 0 1.6 6.4A8 8 0 0 1 4.1 13zm3.4-2H4.1a8 8 0 0 1 5-6.4A15 15 0 0 0 7.5 11zM12 20c-1-1.3-2.3-3.8-2.5-7h5c-.2 3.2-1.5 5.7-2.5 7zm2.9-.6a15 15 0 0 0 1.6-6.4h3.4a8 8 0 0 1-5 6.4z"/></svg>
          corvantela.com.au
        </li>
      </ul>
    </div>
    <div class="edge-band"></div>
  </section>

  <section class="card card--brand" aria-label="Business card, brand side">
    <div class="brand-lockup">
      <span class="brand-dot"></span>
      <p class="brand-name">Wexcombe<br>Educational Group</p>
    </div>
    <div class="base-line"></div>
  </section>

</body>
</html>
```